Master Label Design for Mesa Verdant Products

Looking to update product labels and add consistency across our line with a new master label design. 'Mesa Verdant' has been a trusted name in the health marketplace providing quality herbal and dietary supplements since 1979. We have 8 products in need of a master label design, examples of our current labels are attached, and you can see more at our website, MesaVerdant.com. All 8 products currently have a 160mm x 58mm label size, while 3 products also have a 194mm x 68mm (Sagebrine, Bulb Hour, and Pungara Scentless Garlic).
Also, our logo is only prominent on the EDTA label, but that product is our #1 seller and most recognizable, it is at the artist's discretion what to do with our logo. (attached, if needed).
Please show me only the label designs for "EDTA".
Target Market(s)
-Health-conscious adults over 40 in North America who buy herbal and/or dietary supplements.
-->Cardiovascular health-conscious adults (a.k.a., "heart healthy" adults)
-->Adults with poor cardiovascular health seeking naturopathic/alternative options.
Industry/Entity Type
Health And Wellness
Logo Text
Mesa Verdant
Colors
Designer to choose colors to be used in the design.
Look and feel
Each slider illustrates characteristics of the customer's brand and the style your logo design should communicate.

```html
<!DOCTYPE html>
<html lang="en">
<head>
<meta charset="utf-8">
<title>EDTA Label – Mesa Verdant</title>
<link href="https://fonts.googleapis.com/css2?family=Montserrat:wght@400;600;700&display=swap" rel="stylesheet">
<style>
  :root {
    --backdrop: #9e9e9e;
    --label-yellow: #fdf03e;
    --leaf-light: #6cc24a;
    --leaf-dark: #1f7a2a;
    --brand-teal: #17907f;
    --title-green: #1f8a2e;
    --text-green: #1d6b27;
    --mark-maroon: #8a2748;
    --gold: #c9a24a;
  }
  * { margin: 0; padding: 0; box-sizing: border-box; }
  html, body {
    width: 1200px; height: 825px; overflow: hidden;
    background: var(--backdrop);
    font-family: "Montserrat", Arial, sans-serif;
  }
  /* 160mm x 58mm label, scaled to 1100 x 400 px */
  .label {
    position: absolute; left: 50px; top: 212px;
    width: 1100px; height: 400px;
    background: var(--label-yellow);
    overflow: hidden;
  }
  .label-art { position: absolute; inset: 0; width: 1100px; height: 400px; }
  .front-panel {
    position: absolute; left: 350px; top: 0;
    width: 300px; height: 400px;
    text-align: center;
  }
  .brand-name {
    position: absolute; left: 28px; top: 34px;
    color: var(--brand-teal);
    font-size: 12px; font-weight: 600;
    letter-spacing: 6px; line-height: 17px; text-align: left;
  }
  .brand-name span { display: block; }
  .brand-name span + span { padding-left: 10px; }
  .mark {
    position: absolute; left: 0; top: 90px; width: 300px;
    display: flex; justify-content: center; align-items: center; gap: 9px;
    color: var(--mark-maroon);
    font-size: 20px; font-weight: 600; line-height: 28px;
  }
  .mark-dot { width: 15px; height: 15px; border-radius: 50%; background: var(--mark-maroon); }
  .product-name {
    position: absolute; left: 0; top: 146px; width: 300px;
    color: var(--title-green);
    font-size: 56px; font-weight: 400; letter-spacing: 2px; line-height: 62px;
  }
  .compound {
    position: absolute; left: 0; top: 212px; width: 300px;
    color: var(--title-green); font-size: 10px; font-weight: 600; letter-spacing: 1px;
  }
  .rule {
    position: absolute; left: 20px; top: 236px; width: 260px; height: 2px;
    background: var(--title-green);
  }
  .ingredients {
    position: absolute; left: 0; top: 250px; width: 300px;
    color: var(--text-green); font-size: 12px; font-weight: 700; line-height: 17px;
  }
  .count {
    position: absolute; left: 0; top: 296px; width: 300px;
    color: var(--text-green);
  }
  .count-number { display: block; font-size: 28px; font-weight: 700; line-height: 32px; }
  .count-unit { display: block; font-size: 10px; font-weight: 700; letter-spacing: 1px; }
</style>
</head>
<body>
  <main class="label">
    <svg class="label-art" viewBox="0 0 1100 400" xmlns="http://www.w3.org/2000/svg">
      <defs>
        <linearGradient id="leafTone" x1="0" y1="0" x2="1" y2="1">
          <stop offset="0" stop-color="#6cc24a"/>
          <stop offset="1" stop-color="#1f7a2a"/>
        </linearGradient>
      </defs>
      <polygon class="leaf-panel" role="img" aria-label="Photograph of green herb leaves"
               points="600,0 1100,0 1100,260 870,290" fill="url(#leafTone)"/>
      <polygon class="leaf-panel" role="img" aria-label="Photograph of green herb leaves"
               points="0,190 0,400 300,400 110,180" fill="url(#leafTone)"/>
      <polygon class="light-band" points="615,0 665,0 935,290 885,290" fill="#ffffff" opacity="0.35"/>
      <polygon class="light-band" points="0,290 0,325 70,400 110,400" fill="#ffffff" opacity="0.3"/>
      <g class="gold-lines" stroke="#c9a24a" stroke-width="2" fill="none">
        <line x1="575" y1="0" x2="845" y2="290"/>
        <line x1="555" y1="0" x2="825" y2="290"/>
        <line x1="95" y1="180" x2="290" y2="400"/>
        <polyline points="0,330 40,300 130,400"/>
      </g>
    </svg>

    <section class="front-panel">
      <div class="brand-name"><span>MESA</span><span>VERDANT</span></div>
      <div class="mark"><span class="mark-dot"></span><span>Mesa Verdant</span></div>

      <h1 class="product-name">EDTA</h1>
      <p class="compound">(DISODIUM EDTA)</p>
      <div class="rule"></div>
      <p class="ingredients">WITH YUCCA, VIT. C,<br>ZINC AND ALFALFA</p>
      <p class="count"><span class="count-number">90</span><span class="count-unit">CAPSULES</span></p>
    </section>
  </main>
</body>
</html>
```